Business Card design

Keen on a very modern design with using the red star as a feature point preferably will have it printed with red foiling.

Target Market(s)

Cosmetics

Industry/Entity Type

Cosmetics

Contact Information for Business Card

Marnie Telford
Director
17 Brisbrook Lane
Wyndale Heights Victoria
Australia 3033
marnie@glowcratesupply.com.au

Font styles to use
Sans Serif

Colors
ec1f27
000000

Requirements
Must have
• Keen on some red stars on back with black background and I may get the red components printed as red foiling potentially

```html
<!DOCTYPE html>
<html lang="en">
<head>
<meta charset="utf-8">
<title>Glowcrate Business Card</title>
<link rel="stylesheet" href="https://fonts.googleapis.com/css2?family=Arimo:wght@400;700&display=swap">
<style>
  :root {
    --brand-red: #ec1f27;
    --brand-black: #000000;
    --card-white: #ffffff;
    --card-edge: #8a8a8a;
    --page-bg: #ffffff;
  }
  html, body {
    margin: 0;
    padding: 0;
    width: 1200px;
    height: 729px;
    overflow: hidden;
    background: var(--page-bg);
  }
  .canvas {
    position: relative;
    width: 1200px;
    height: 729px;
    font-family: "Arimo", Arial, sans-serif;
  }
  .card {
    position: absolute;
    width: 484px;
    height: 294px;
    background: var(--card-white);
    outline: 1px solid var(--card-edge);
    overflow: hidden;
  }
  .card--front { left: 73px; top: 224px; }
  .card--back  { left: 666px; top: 225px; }
  .card svg { display: block; width: 100%; height: 100%; }
  .shape-red   { fill: var(--brand-red); }
  .shape-black { fill: var(--brand-black); }
  .brand-name {
    font-family: "Arimo", Arial, sans-serif;
    font-weight: 700;
    fill: var(--brand-black);
    letter-spacing: -1px;
  }
  .brand-dot { fill: var(--brand-red); }
  .contact {
    font-family: "Arimo", Arial, sans-serif;
    font-weight: 400;
    fill: var(--brand-black);
  }
  .contact-name  { font-size: 26px; }
  .contact-title { font-size: 14px; }
  .contact-line  { font-size: 21.5px; }
</style>
</head>
<body>
<main class="canvas">

  <section class="card card--front" aria-label="Card front">
    <svg viewBox="0 0 605 367" preserveAspectRatio="none">
      <polygon class="shape-black" points="261,0 395,0 266,42"/>
      <polygon class="shape-black" points="219,194 349,367 261,367 64,318"/>
      <polygon class="shape-red" points="141,367 154,341 261,367"/>
      <polygon class="shape-red" points="0,106 460,0 0,367"/>
      <rect class="brand-dot" x="322" y="178" width="26" height="26"/>
      <text class="brand-name" x="567" y="208" text-anchor="end" font-size="44">Glowcrate</text>
    </svg>
  </section>

  <section class="card card--back" aria-label="Card back">
    <svg viewBox="0 0 605 367" preserveAspectRatio="none">
      <polygon class="shape-black" points="34,0 92,0 60,110 0,282 0,100"/>
      <polygon class="shape-red" points="75,0 313,0 0,137 0,108"/>
      <text class="contact contact-name" x="560" y="104" text-anchor="end">MARNIE TELFORD</text>
      <text class="contact contact-title" x="560" y="124" text-anchor="end">Director</text>
      <text class="contact contact-line" x="560" y="177" text-anchor="end">17 Brisbrook Lane</text>
      <text class="contact contact-line" x="560" y="204" text-anchor="end">Wyndale Heights Victoria</text>
      <text class="contact contact-line" x="560" y="230" text-anchor="end">Australia 3033</text>
      <text class="contact contact-line" x="560" y="257" text-anchor="end">marnie@glowcratesupply.com.au</text>
      <rect class="brand-dot" x="452" y="271" width="12" height="12"/>
      <text class="brand-name" x="560" y="284" text-anchor="end" font-size="18" letter-spacing="-0.5">Glowcrate</text>
    </svg>
  </section>

</main>
</body>
</html>
```